Body therapist needs a business card

I need a card for my business which is teaching trainings in body therapy, the company is called Wexcombe Educational Group. I teach to massage therapists around Australia, South East Asia and the USA. I am attaching my logo which will guide you as to what colours I would like to have you consider. Please consult my website to find out more about what I do. www.corvantela.com.au

My name is Daniel Wexcombe. My phone number is (03) 9417 2608 or 0461753208. email is info@corvantela.com.au

```html
<!DOCTYPE html>
<html lang="en">
<head>
<meta charset="utf-8">
<title>Wexcombe Educational Group – Business Card</title>
<link rel="stylesheet" href="https://fonts.googleapis.com/css2?family=Open+Sans:wght@300;400;700;800&display=swap">
<style>
  :root {
    --stage: #5c5c5c;
    --card-front: #ffffff;
    --card-back: #ebe3dc;
    --brown: #8a4a1f;
    --red: #b3161f;
    --navy: #222b33;
    --ink: #1c1c1c;
    --grey: #6b6b6b;
    --rule: #c9c9c9;
  }
  * { box-sizing: border-box; margin: 0; padding: 0; }
  html, body {
    width: 1200px; height: 1200px; overflow: hidden;
    background: var(--stage);
    font-family: "Open Sans", Arial, sans-serif;
  }
  .card {
    position: absolute; left: 180px;
    width: 840px; height: 480px;
    border-radius: 18px; overflow: hidden;
  }
  .card--front { top: 90px; background: var(--card-front); }
  .card--back { top: 630px; background: var(--card-back); }

  .brand { position: absolute; left: 64px; top: 60px; display: flex; align-items: center; gap: 26px; }
  .brand__dot { width: 112px; height: 112px; border-radius: 50%; background: var(--brown); }
  .brand__name { color: var(--brown); font-weight: 400; line-height: 1.05; }
  .brand__name .line1 { display: block; font-size: 46px; }
  .brand__name .line2 { display: block; font-size: 24px; padding-left: 4px; }

  .person { position: absolute; left: 300px; top: 200px; }
  .person__name { color: var(--brown); font-size: 31px; font-weight: 800; }
  .person__role { color: var(--grey); font-size: 19px; margin-top: 2px; padding-left: 6px; }

  .contact { position: absolute; left: 318px; top: 288px; list-style: none; }
  .contact li { display: flex; align-items: center; gap: 10px; font-size: 19px; color: var(--ink); line-height: 30px; }
  .contact svg { width: 17px; height: 17px; fill: var(--ink); }

  .divider { position: absolute; left: 600px; top: 262px; width: 1px; height: 66px; background: var(--rule); }

  .address { position: absolute; left: 622px; top: 258px; display: flex; gap: 12px; font-size: 18px; color: var(--ink); line-height: 27px; }
  .address svg { width: 16px; height: 20px; fill: var(--ink); margin-top: 4px; }
  .address span { display: block; }
  .address .indent { padding-left: 14px; }

  .website { position: absolute; right: 52px; top: 352px; font-size: 31px; color: var(--ink); letter-spacing: 0.5px; }
  .website strong { font-weight: 800; }
  .website .light { font-weight: 400; }

  .footer-band { position: absolute; left: 0; bottom: 0; width: 100%; height: 24px; background: var(--brown); }
  .abn-tab {
    position: absolute; left: 0; bottom: 24px; width: 470px; height: 54px;
    background: var(--navy); border-top-right-radius: 26px;
    color: #fff; font-size: 17px; display: flex; align-items: center; justify-content: flex-end; padding-right: 40px;
  }

  .back-brand { position: absolute; inset: 0; display: flex; align-items: center; justify-content: center; gap: 26px; }
  .back-brand__dot { width: 150px; height: 150px; border-radius: 50%; background: var(--brown); }
  .back-brand__name { color: var(--brown); font-size: 40px; font-weight: 400; line-height: 1.1; }
</style>
</head>
<body>
  <section class="card card--front" aria-label="Business card front">
    <div class="brand">
      <div class="brand__dot"></div>
      <div class="brand__name"><span class="line1">Wexcombe</span><span class="line2">Educational Group</span></div>
    </div>

    <div class="person">
      <h1 class="person__name">Daniel Wexcombe</h1>
      <p class="person__role">Business Manager</p>
    </div>

    <ul class="contact">
      <li>
        <svg viewBox="0 0 24 24" aria-hidden="true"><path d="M6.6 10.8a15.1 15.1 0 0 0 6.6 6.6l2.2-2.2a1 1 0 0 1 1-.25 11.4 11.4 0 0 0 3.6.57 1 1 0 0 1 1 1V20a1 1 0 0 1-1 1A17 17 0 0 1 3 4a1 1 0 0 1 1-1h3.5a1 1 0 0 1 1 1c0 1.25.2 2.45.57 3.57a1 1 0 0 1-.25 1z"/></svg>
        (03) 9417 2608
      </li>
      <li>
        <svg viewBox="0 0 24 24" aria-hidden="true"><path d="M2 5h20v14H2zm2 2v.5l8 5 8-5V7zm0 3v7h16v-7l-8 5z"/></svg>
        info@corvantela.com.au
      </li>
    </ul>

    <div class="divider"></div>

    <div class="address">
      <svg viewBox="0 0 16 20" aria-hidden="true"><path d="M8 0a7 7 0 0 0-7 7c0 5 7 13 7 13s7-8 7-13a7 7 0 0 0-7-7zm0 10a3 3 0 1 1 0-6 3 3 0 0 1 0 6z"/></svg>
      <div><span>Brellin North</span><span class="indent">Victoria, 3187 Australia</span></div>
    </div>

    <p class="website"><span class="light">www.</span><strong>corvantela</strong><span class="light">.com.au</span></p>

    <div class="abn-tab">ABN: 42 816 093 254</div>
    <div class="footer-band"></div>
  </section>

  <section class="card card--back" aria-label="Business card back">
    <div class="back-brand">
      <div class="back-brand__dot"></div>
      <div class="back-brand__name">Wexcombe<br>Educational Group</div>
    </div>
  </section>
</body>
</html>
```